Kestrel Plumbing business card full re design & logo design

Kestrel Plumbing is a Sydney based mechanical plumbing contractor company.
We would like a full redesign with new logo etc which we can take to a future website, uniforms, vehicle sign writing etc.
Blue is my preferred choice of colour but i would be open to see a couple of alternatives thrown in the mix to see how they compare. I am open to see on white cards, black cards etc. Open to many new ideas.
Please see attached original business cards which have been used for the last 5 years.

Target Market(s)

Mechanical services industry.

Industry/Entity Type

Plumbing

Contact Information for Business Card

Dale Fenmore
Director

Mob: 0427 596 418
Email: dale@kestrelplumbing-demo.net.au
PO BOX 782
Merrowvale NSW 2199
Lic: 518604k

Logo Text

Kestrel Plumbing

Font styles to use
Sans Serif

Colors
0655a3
3276b5
0792cd
33a6d7
85cae6
000000
333333
474747

Requirements
Must have
• Things that make it very professional and very well presented.
Nice to have
• Same description or very similar to attached uploaded file
Should not have
• Anything that makes it look unprofessional or cartoony.

```html
<!DOCTYPE html>
<html lang="en">
<head>
<meta charset="utf-8">
<title>Kestrel Plumbing Business Card</title>
<link href="https://fonts.googleapis.com/css2?family=Rubik:wght@400;500;700&display=swap" rel="stylesheet">
<style>
  :root {
    --blue-deep: #0655a3;
    --blue-mid: #3276b5;
    --blue-bright: #0792cd;
    --blue-light: #33a6d7;
    --blue-pale: #85cae6;
    --ink: #000000;
    --ink-soft: #333333;
    --ink-grey: #474747;
    --paper: #f6f6f4;
    --stage: #dfeef6;
  }
  * { margin: 0; padding: 0; box-sizing: border-box; }
  html, body { width: 1200px; height: 900px; overflow: hidden; }
  body {
    background: var(--stage);
    font-family: "Rubik", sans-serif;
    position: relative;
  }
  .card {
    position: absolute;
    width: 540px;
    height: 310px;
    border-radius: 4px;
    overflow: hidden;
    box-shadow: 0 6px 18px rgba(6, 85, 163, 0.18);
  }

  /* Front */
  .card-front {
    left: 60px;
    top: 110px;
    background: linear-gradient(115deg, var(--blue-pale) 0%, var(--blue-light) 35%, var(--blue-bright) 62%, var(--blue-deep) 100%);
    color: #fff;
  }
  .front-brand {
    position: absolute;
    left: 120px;
    top: 92px;
    display: flex;
    align-items: center;
    gap: 16px;
  }
  .brand-square {
    width: 44px;
    height: 44px;
    background: #fff;
  }
  .front-brand .brand-name {
    font-weight: 700;
    font-size: 44px;
    line-height: 0.95;
    letter-spacing: -0.5px;
    text-transform: uppercase;
    color: #fff;
  }
  .front-brand .brand-name span {
    display: block;
    font-size: 20px;
    letter-spacing: 6px;
    margin-top: 4px;
  }
  .tagline {
    position: absolute;
    left: 120px;
    top: 210px;
    font-weight: 500;
    font-size: 17px;
    letter-spacing: 1.5px;
    color: #fff;
  }
  .tagline .soft { text-transform: none; }

  /* Back */
  .card-back {
    left: 600px;
    top: 480px;
    background: var(--paper);
  }
  .back-brand {
    position: absolute;
    left: 30px;
    top: 28px;
    display: flex;
    align-items: center;
    gap: 12px;
  }
  .back-brand .brand-square { width: 34px; height: 34px; background: var(--blue-bright); }
  .back-brand .brand-name {
    font-weight: 700;
    font-size: 30px;
    line-height: 0.95;
    text-transform: uppercase;
    color: var(--ink-soft);
  }
  .back-brand .brand-name span {
    display: block;
    font-size: 14px;
    letter-spacing: 5px;
    margin-top: 3px;
  }
  .contact {
    position: absolute;
    left: 30px;
    top: 96px;
  }
  .contact-name { font-weight: 700; font-size: 22px; color: var(--blue-bright); }
  .contact-role { font-weight: 500; font-size: 12px; color: var(--ink); margin: 2px 0 6px; }
  .contact-line { font-weight: 500; font-size: 12px; color: var(--ink); line-height: 1.45; }
  .contact-line b { color: var(--blue-light); font-weight: 500; margin-right: 4px; }
  .postal {
    position: absolute;
    right: 34px;
    top: 34px;
    font-weight: 500;
    font-size: 12px;
    line-height: 1.4;
    color: var(--ink);
  }
  .postal b { color: var(--blue-light); font-weight: 500; }
  .services-band {
    position: absolute;
    left: 0;
    right: 0;
    top: 182px;
    height: 74px;
    background: linear-gradient(90deg, var(--blue-pale) 0%, var(--blue-light) 40%, var(--blue-mid) 75%, var(--blue-deep) 100%);
    padding: 10px 30px;
    color: #fff;
  }
  .services-title {
    font-weight: 700;
    font-size: 12px;
    letter-spacing: 0.4px;
    padding-bottom: 4px;
    border-bottom: 1.5px solid #fff;
    display: inline-block;
    margin-bottom: 5px;
  }
  .services-list { font-weight: 500; font-size: 12px; line-height: 1.4; }
  .website {
    position: absolute;
    right: 34px;
    bottom: 18px;
    font-weight: 700;
    font-size: 16px;
    letter-spacing: 0.6px;
    color: var(--blue-bright);
  }
</style>
</head>
<body>

<section class="card card-front" aria-label="Card front">
  <div class="front-brand">
    <div class="brand-square"></div>
    <div class="brand-name">Kestrel<span>Plumbing</span></div>
  </div>
  <p class="tagline">KESTREL <span class="soft">have the</span> SOLUTION</p>
</section>

<section class="card card-back" aria-label="Card back">
  <div class="back-brand">
    <div class="brand-square"></div>
    <div class="brand-name">Kestrel<span>Plumbing</span></div>
  </div>

  <div class="contact">
    <p class="contact-name">Dale Fenmore</p>
    <p class="contact-role">Director</p>
    <p class="contact-line"><b>M:</b>0427 596 418</p>
    <p class="contact-line"><b>E:</b>dale@kestrelplumbing-demo.net.au</p>
  </div>

  <div class="postal">
    <p>PO BOX 782</p>
    <p>Merrowvale NSW 2199</p>
    <p><b>Lic:</b> 518604k</p>
  </div>

  <div class="services-band">
    <p class="services-title">MECHANICAL PLUMBING SERVICES</p>
    <p class="services-list">Make Good // Refurbishments // Tenancy Fit out</p>
    <p class="services-list">Plant Room Works // Shut Downs // Change Overs</p>
  </div>

  <p class="website">www.kestrelplumbing-demo.net.au</p>
</section>

</body>
</html>
```